Breast Cancer Fashion Show & Dinner,

Need a postcard flyer to describe event and sell it. Needs to give info and make the flyer pop out and be very trendy and in line with our event
Fashion Show to celebrate Breast Cancer Survivors, honors those who haven't and support newly diagnosed.
#ootd (outfit of the day) Featuring casual everyday wear blended with up cycling and repourposed clothing.

Target Market(s)

30-65 year old women who drink wine

Colors
E54698
E96AAD
F1A4CE
F9D9EA
FCEFF6

Requirements
Must have
• hosting companies logos, date/time, ticket price, qr code, contact info and link
Nice to have
• Event Name : Dance Under Dusk

```html
<!DOCTYPE html>
<html lang="en">
<head>
<meta charset="utf-8">
<title>Dance Under Dusk – Fashion Show &amp; Dinner</title>
<link rel="stylesheet" href="https://fonts.googleapis.com/css2?family=Barlow+Semi+Condensed:wght@400;500;600;700&family=Fredoka:wght@500&family=Dancing+Script:wght@600&display=swap">
<style>
  :root {
    --page: #ffffff;
    --card: #e6819c;
    --card-light: #f1a4c0;
    --rose-deep: #bf5470;
    --rose-dark: #a9445f;
    --footer: #c2566f;
    --white: #ffffff;
    --blush: #f9d9ea;
  }
  * { box-sizing: border-box; margin: 0; padding: 0; }
  html, body {
    width: 1200px; height: 1177px; overflow: hidden;
    background: var(--page);
    font-family: "Barlow Semi Condensed", "Arial Narrow", sans-serif;
  }
  .postcard {
    position: absolute; left: 60px; top: 228px;
    width: 1080px; height: 720px; overflow: hidden;
    background: linear-gradient(120deg, #e8859f 0%, var(--card) 45%, #e27b97 100%);
  }
  .ribbon-art { position: absolute; left: 0; top: 90px; width: 620px; height: 580px; }
  .date {
    position: absolute; left: 38px; top: 40px;
    display: flex; align-items: center; gap: 14px; color: var(--rose-deep);
  }
  .date-day { font-size: 96px; font-weight: 700; line-height: 1; letter-spacing: -2px; }
  .date-meta { font-size: 29px; font-weight: 600; line-height: 1.2; }
  .date-month { border-bottom: 2px solid var(--rose-deep); padding-bottom: 2px; margin-bottom: 4px; }
  .header-band {
    position: absolute; left: 320px; top: 28px; width: 760px; height: 54px;
    background: linear-gradient(90deg, rgba(249,217,234,0) 0%, rgba(249,217,234,.35) 25%, rgba(249,217,234,.35) 70%, rgba(249,217,234,0) 100%);
    display: flex; align-items: center; padding-left: 48px;
    color: var(--white); font-size: 30px; font-weight: 500; letter-spacing: .5px;
  }
  .header-band .amp { font-family: "Dancing Script", cursive; font-size: 30px; margin: 0 8px; }
  .event-title {
    position: absolute; left: 344px; top: 104px; max-width: 700px;
    font-family: "Fredoka", sans-serif; font-weight: 500;
    font-size: 72px; line-height: 1; color: var(--white); white-space: nowrap;
  }
  .event-summary {
    position: absolute; left: 350px; top: 238px; width: 425px;
    color: var(--white); font-size: 21px; line-height: 27px;
  }
  .ticket {
    position: absolute; left: 350px; top: 370px;
    color: var(--rose-dark); font-size: 22px; font-weight: 700;
  }
  .hashtag {
    position: absolute; left: 350px; top: 404px; width: 118px; height: 40px;
    background: var(--rose-deep); border: 2px solid var(--blush); border-radius: 4px;
    color: var(--white); font-size: 27px; font-weight: 600;
    display: flex; align-items: center; justify-content: center;
  }
  .hosts {
    position: absolute; left: 250px; top: 500px;
    display: flex; gap: 22px; align-items: center;
  }
  .host { display: flex; align-items: center; gap: 6px; color: var(--rose-dark); font-size: 18px; font-weight: 700; }
  .host-dot { width: 16px; height: 16px; border-radius: 50%; background: var(--rose-dark); }
  .qr-slot {
    position: absolute; left: 56px; top: 562px; width: 86px; height: 86px;
    border: 2px solid var(--rose-deep);
    color: var(--rose-deep); font-size: 17px; font-weight: 500; line-height: 1.3;
    display: flex; align-items: center; justify-content: center; text-align: center;
  }
  .photo-frame {
    position: absolute; left: 690px; top: 210px; width: 680px; height: 680px;
    border-radius: 50%; border: 3px solid var(--white);
    background: radial-gradient(circle at 40% 45%, #f7dbe6 0%, #eab3c6 45%, #e38ca8 100%);
  }
  .footer {
    position: absolute; left: 0; bottom: 0; width: 100%; height: 70px;
    background: var(--footer); color: var(--white);
    display: flex; align-items: center; padding-left: 56px;
    font-size: 23px; font-weight: 500; white-space: nowrap;
  }
  .footer b { font-weight: 700; }
  .footer .divider { margin: 0 22px; }
</style>
</head>
<body>
  <main class="postcard">
    <svg class="ribbon-art" role="img" aria-label="Pink awareness ribbon illustration" viewBox="0 0 620 580">
      <defs>
        <radialGradient id="ribbonGlow" cx="45%" cy="50%" r="55%">
          <stop offset="0%" stop-color="#f9d9ea" stop-opacity=".75"/>
          <stop offset="60%" stop-color="#f1a4c0" stop-opacity=".45"/>
          <stop offset="100%" stop-color="#e6819c" stop-opacity="0"/>
        </radialGradient>
      </defs>
      <ellipse cx="260" cy="300" rx="300" ry="280" fill="url(#ribbonGlow)"/>
    </svg>

    <div class="date">
      <span class="date-day">DD</span>
      <div class="date-meta">
        <div class="date-month">MONTH 2022</div>
        <div class="date-time">TIME</div>
      </div>
    </div>

    <div class="header-band">BREAST CANCER FASHION SHOW <span class="amp">&amp;</span> DINNER</div>

    <h1 class="event-title">Dance Under Dusk</h1>

    <p class="event-summary">Fashion Show to celebrate Breast Cancer Survivors, honors those who haven't &amp; support newly diagnosed. Featuring casual everyday wear blended with up cycling and repourposed clothing.</p>

    <p class="ticket">TICKET: 100 USD</p>
    <div class="hashtag">#OOTD</div>

    <div class="hosts">
      <div class="host"><span class="host-dot"></span>Harbor Vine</div>
      <div class="host"><span class="host-dot"></span>Circle Square</div>
    </div>

    <div class="qr-slot">QR<br>CODE</div>

    <div class="photo-frame" role="img" aria-label="Photo of two smiling women in casual summer outfits"></div>

    <footer class="footer">
      <span>Link: www.<b>website</b>.com</span>
      <span class="divider">|</span>
      <span>For more information contact : <b>NAME</b> at <b>987654321</b> or <b>name@email.com</b></span>
    </footer>
  </main>
</body>
</html>
```